Business Card Design Project

I need a business card design for our new logo, please check the logo at the following link:
https://www.filecrate.net/s/q7rtx2pw9kd41m/FernLoop.png
The address on the business card:
Av. Gervásio Tavares 418 sala 207
Barra da Tijuca, Rio de Janeiro, RJ
CEP: 22714-380
Brasil
Phone: +55 21 86347215
e-mail: osvaldo@fernloop.com.br
Updates
Thank you all for sending your designs, we will not provide feedback because there are too many designs, on December 3 we will pick the best design according to our point of view. Please keep posting.
Osvaldo
Industry/Entity Type
Business
Look and feel
Each slider illustrates characteristics of the customer's brand and the style your logo design should communicate.

```html
<!DOCTYPE html>
<html lang="pt-BR">
<head>
<meta charset="utf-8">
<title>FernLoop – Business Card</title>
<link rel="stylesheet" href="https://fonts.googleapis.com/css2?family=Exo+2:wght@400;500;700;800&display=swap">
<style>
  :root {
    --page-bg: #3a3a3c;
    --card-white: #f4f4f4;
    --card-white-shade: #e2e2e2;
    --mosaic-light: #d9d4d1;
    --mosaic-dark: #9c9592;
    --ink: #1e1e1e;
    --ink-soft: #3a3a3a;
    --rule: #b9b9b9;
    --accent: #f2c20f;
    --band: #1a1a1a;
  }
  * { margin: 0; padding: 0; box-sizing: border-box; }
  html, body { width: 1200px; height: 871px; overflow: hidden; }
  body {
    background: var(--page-bg);
    font-family: "Exo 2", sans-serif;
    color: var(--ink);
    position: relative;
  }
  .card {
    position: absolute;
    top: 281px;
    width: 540px;
    height: 309px;
    overflow: hidden;
    border-radius: 2px;
  }
  .card--back { left: 40px; }
  .card--front { left: 620px; background: linear-gradient(160deg, var(--card-white) 40%, var(--card-white-shade)); }

  /* back side */
  .mosaic {
    position: absolute; inset: 0;
    background: radial-gradient(ellipse at 35% 40%, var(--mosaic-light) 0%, #c2bcb9 50%, var(--mosaic-dark) 100%);
  }
  .back-brand {
    position: absolute; left: 0; right: 0; top: 118px;
    display: flex; justify-content: center; align-items: center; gap: 14px;
  }
  .brand-mark { width: 46px; height: 46px; background: var(--accent); }
  .brand-name { font-weight: 800; font-size: 46px; color: var(--ink); letter-spacing: 0.5px; }
  .back-url {
    position: absolute; left: 0; right: 0; top: 186px;
    text-align: center; font-size: 13px; font-weight: 500; color: var(--accent);
  }

  /* front side */
  .front-brand {
    position: absolute; left: 40px; top: 82px;
    display: flex; align-items: center; gap: 14px;
  }
  .front-brand .brand-mark { width: 40px; height: 40px; }
  .front-brand .brand-name { font-size: 38px; }
  .person { position: absolute; left: 40px; top: 198px; width: 230px; }
  .person-name { font-size: 20px; font-weight: 500; letter-spacing: 0.5px; }
  .person-role { font-size: 11px; font-weight: 400; color: var(--ink-soft); margin-left: 3px; }
  .person-rule { height: 1px; background: var(--rule); margin: 5px 0 8px; }
  .contact-row { font-size: 13px; line-height: 19px; white-space: nowrap; }
  .contact-label { color: var(--accent); display: inline-block; width: 44px; font-size: 12px; }
  .address {
    position: absolute; left: 296px; top: 150px;
    font-size: 13px; line-height: 19px; color: var(--ink);
  }
  .address .country { padding-left: 10px; }
  .edge { position: absolute; left: 0; bottom: 0; }
</style>
</head>
<body>

<section class="card card--back" aria-label="Card back">
  <div class="mosaic" role="img" aria-label="Soft grey square mosaic background pattern"></div>
  <div class="back-brand">
    <span class="brand-mark"></span>
    <span class="brand-name">FernLoop</span>
  </div>
  <p class="back-url">www.FernLoop.com.br</p>
</section>

<section class="card card--front" aria-label="Card front">
  <div class="front-brand">
    <span class="brand-mark"></span>
    <span class="brand-name">FernLoop</span>
  </div>

  <div class="person">
    <p><span class="person-name">JOHN DOE</span><span class="person-role">Manager</span></p>
    <div class="person-rule"></div>
    <p class="contact-row"><span class="contact-label">phone</span>+55 21 86347215</p>
    <p class="contact-row"><span class="contact-label">e-mail</span>osvaldo@fernloop.com.br</p>
  </div>

  <address class="address" style="font-style:normal">
    Av. Gervásio Tavares 418 sala 207<br>
    Barra da Tijuca, Rio de Janeiro, RJ<br>
    CEP: 22714-380<br>
    <span class="country">Brasil</span>
  </address>

  <svg class="edge" width="540" height="309" viewBox="0 0 540 309" aria-hidden="true">
    <polygon points="0,282 24,282 32,292 540,292 540,309 0,309" fill="var(--band)"/>
    <polygon points="400,268 540,268 540,280 390,280" fill="var(--accent)"/>
  </svg>
</section>

</body>
</html>
```